KORBALT

The business want a professional looking business card. We have a scetch we will add but want the extra upgrade, and would like more suggestions for variations of our business cards.

```html
<!DOCTYPE html>
<html lang="en">
<head>
<meta charset="utf-8">
<title>KORBALT Business Card</title>
<link href="https://fonts.googleapis.com/css2?family=Playfair+Display:wght@700;900&family=Lato:wght@400&display=swap" rel="stylesheet">
<style>
  :root {
    --backdrop: #8e8e8e;
    --card-black: #0b0b0b;
    --card-charcoal: #1c1c1c;
    --gold: #d9b35a;
    --gold-light: #f6dc9a;
    --gold-deep: #9c7426;
    --text-light: #e6e6e6;
  }
  * { margin: 0; padding: 0; box-sizing: border-box; }
  html, body { width: 1200px; height: 1200px; overflow: hidden; background: var(--backdrop); }
  .canvas { position: relative; width: 1200px; height: 1200px; }

  .card {
    position: absolute; left: 281px; width: 641px; height: 366px;
    border-radius: 18px; overflow: hidden;
    background: linear-gradient(180deg, var(--card-black) 0%, var(--card-charcoal) 55%, var(--card-black) 100%);
  }
  .card--front { top: 195px; }
  .card--back { top: 639px; }

  .card__wave { position: absolute; left: 0; top: 0; width: 641px; height: 366px; }

  .brand {
    position: absolute; left: 70px; top: 110px; width: 160px; height: 140px;
    display: flex; flex-direction: column; align-items: center; justify-content: center; gap: 10px;
  }
  .brand__dot { width: 14px; height: 14px; border-radius: 50%; background: var(--gold); }
  .brand__name {
    font-family: "Playfair Display", serif; font-weight: 700; font-size: 28px;
    letter-spacing: 2px; color: var(--gold);
  }
  .brand__since {
    font-family: "Lato", sans-serif; font-size: 9px; letter-spacing: 4px; color: var(--gold);
  }

  .divider { position: absolute; left: 247px; top: 103px; width: 1px; height: 138px; background: var(--gold); }

  .person { position: absolute; left: 282px; top: 98px; }
  .person__name {
    font-family: "Playfair Display", serif; font-weight: 900; font-size: 25px;
    color: var(--gold); line-height: 1.1;
  }
  .person__role { font-family: "Lato", sans-serif; font-size: 16px; color: var(--text-light); margin-top: 4px; }

  .contact { position: absolute; left: 282px; top: 180px; list-style: none; }
  .contact__item {
    display: flex; align-items: center; gap: 12px; height: 22.5px;
    font-family: "Lato", sans-serif; font-size: 14.5px; color: var(--text-light);
  }
  .contact__icon { width: 12px; height: 12px; flex: none; }

  .pattern {
    position: absolute; border-radius: 6px;
    background: linear-gradient(180deg, rgba(156,116,38,0.45), rgba(217,179,90,0.85));
  }
  .pattern--top { left: 12px; top: 14px; width: 617px; height: 110px; background: linear-gradient(180deg, rgba(110,82,30,0.45), rgba(156,116,38,0.6)); }
  .pattern--left { left: 12px; top: 130px; width: 112px; height: 104px; }
  .pattern--right { left: 653px; }
  .pattern--right-block { left: 517px; top: 130px; width: 112px; height: 104px; }
  .pattern--bottom { left: 12px; top: 240px; width: 617px; height: 112px; background: linear-gradient(180deg, rgba(217,179,90,0.85), rgba(200,160,70,0.8)); }

  .wordmark {
    position: absolute; left: 130px; top: 136px; width: 381px; text-align: center;
    font-family: "Playfair Display", serif; font-weight: 700; font-size: 70px;
    line-height: 1; letter-spacing: 2px; color: var(--gold);
  }
  .tagline {
    position: absolute; left: 132px; top: 214px; width: 377px;
    display: flex; align-items: center; gap: 14px;
    font-family: "Lato", sans-serif; font-size: 20px; letter-spacing: 10px; color: var(--gold);
  }
  .tagline__rule { flex: 1; height: 2px; background: var(--gold); }
</style>
</head>
<body>
<main class="canvas">

  <section class="card card--front" aria-label="Business card front">
    <svg class="card__wave" viewBox="0 0 641 366" aria-hidden="true">
      <defs>
        <linearGradient id="goldBand" x1="0" y1="0" x2="0" y2="1">
          <stop offset="0" stop-color="#9c7426"/>
          <stop offset="0.5" stop-color="#e3c172"/>
          <stop offset="1" stop-color="#fbe3a6"/>
        </linearGradient>
      </defs>
      <path d="M0 290 Q320 370 641 285 L641 366 L0 366 Z" fill="url(#goldBand)"/>
      <path d="M0 270 Q260 350 560 330 Q300 352 0 300 Z" fill="#050505"/>
    </svg>

    <div class="brand">
      <span class="brand__dot"></span>
      <span class="brand__name">KORBALT</span>
      <span class="brand__since">SINCE 2026</span>
    </div>

    <div class="divider"></div>

    <div class="person">
      <p class="person__name">Anders Lunde Haugen</p>
      <p class="person__role">CEO &amp; Founder</p>
    </div>

    <ul class="contact">
      <li class="contact__item">
        <svg class="contact__icon" viewBox="0 0 12 12" aria-hidden="true"><path d="M2.5 1 L4.5 1 L5.2 3.5 L4 4.5 Q5 7 7.5 8 L8.5 6.8 L11 7.5 L11 9.5 Q11 11 9.5 11 Q1 10 1 2.5 Q1 1 2.5 1 Z" fill="#d9b35a"/></svg>
        004791234567
      </li>
      <li class="contact__item">
        <svg class="contact__icon" viewBox="0 0 12 12" aria-hidden="true"><rect x="0.5" y="2.5" width="11" height="7.5" fill="#d9b35a"/><path d="M0.5 2.5 L6 7 L11.5 2.5" fill="none" stroke="#1c1c1c" stroke-width="1"/></svg>
        korbalt.llc@postmail.com
      </li>
      <li class="contact__item">
        <svg class="contact__icon" viewBox="0 0 12 12" aria-hidden="true"><circle cx="6" cy="6" r="5.5" fill="#d9b35a"/><path d="M1 6 H11 M6 0.5 V11.5" stroke="#1c1c1c" stroke-width="0.9"/></svg>
        www.korbalt.llc
      </li>
    </ul>
  </section>

  <section class="card card--back" aria-label="Business card back">
    <div class="pattern pattern--top" role="img" aria-label="Repeating gold ornamental pattern"></div>
    <div class="pattern pattern--left" role="img" aria-label="Repeating gold ornamental pattern"></div>
    <div class="pattern pattern--right-block" role="img" aria-label="Repeating gold ornamental pattern"></div>
    <div class="pattern pattern--bottom" role="img" aria-label="Repeating gold ornamental pattern"></div>

    <p class="wordmark">KORBALT</p>
    <div class="tagline">
      <span class="tagline__rule"></span>
      <span>SINCE 2026</span>
      <span class="tagline__rule"></span>
    </div>
  </section>

</main>
</body>
</html>
```